Company Business Card

I need a Business card designed for my granite company(We install and supply Granite Counter tops). It just needs to have the employee name, title, Store address, email, and phone number. With a nifty logo design and preferably our Maplio map location on the backside. I am not creative so you can go crazy or simple on the logo.
Company Name : The Stone Harbor
Employee Name: Martin Cole
Title: Owner
Address: 4832 Fenwick Oaks Blvd. Dallas, Texas 75391
Email: Martin.Cole@SHBexample.com
Phone: 214-555-0183

```html
<!DOCTYPE html>
<html lang="en">
<head>
<meta charset="utf-8">
<title>The Stone Harbor – Business Card</title>
<link href="https://fonts.googleapis.com/css2?family=Open+Sans:wght@600;700&family=Noto+Serif:wght@400&display=swap" rel="stylesheet">
<style>
  :root {
    --backdrop: #7a5536;
    --card: #ffffff;
    --green: #1f8a1f;
    --gold: #f4b120;
    --ink: #222222;
    --divider: #d6d6d6;
    --map-base: #e6e2d6;
    --map-park: #c9dcae;
  }
  * { margin: 0; padding: 0; box-sizing: border-box; }
  html, body { width: 1200px; height: 447px; overflow: hidden; }
  body {
    background: var(--backdrop);
    position: relative;
    font-family: "Noto Serif", Georgia, serif;
  }
  .card {
    position: absolute;
    top: 68px;
    width: 540px;
    height: 310px;
    background: var(--card);
    overflow: hidden;
    box-shadow: 0 6px 18px rgba(0,0,0,.35);
  }
  .card--front { left: 40px; }
  .card--back { left: 620px; }

  /* Front */
  .brand {
    position: absolute;
    left: 40px;
    top: 110px;
    width: 230px;
    display: flex;
    align-items: center;
    gap: 10px;
  }
  .brand__square {
    width: 26px; height: 26px;
    background: var(--gold);
    flex: none;
  }
  .brand__name {
    font-family: "Open Sans", Arial, sans-serif;
    font-weight: 700;
    font-size: 24px;
    line-height: 1.1;
    color: var(--green);
  }
  .divider {
    position: absolute;
    left: 285px; top: 40px;
    width: 1px; height: 135px;
    background: var(--divider);
  }
  .person { position: absolute; left: 310px; top: 40px; }
  .person__name { font-size: 22px; color: var(--green); line-height: 1.1; }
  .person__title { font-size: 15px; color: var(--gold); margin-top: 2px; }
  .contact {
    position: absolute;
    left: 310px; top: 125px;
    list-style: none;
    font-size: 13px;
    color: var(--ink);
  }
  .contact li { display: flex; align-items: center; gap: 6px; margin-bottom: 6px; }
  .contact svg { width: 12px; height: 12px; flex: none; }
  .wave { position: absolute; inset: 0; }
  .address {
    position: absolute;
    left: 100px; top: 262px;
    color: #ffffff;
    font-size: 13px;
    line-height: 1.45;
  }

  /* Back */
  .brand--back {
    left: 40px; top: 70px;
    width: 220px;
    flex-direction: column;
    align-items: flex-start;
    gap: 12px;
  }
  .brand--back .brand__square { width: 40px; height: 40px; }
  .brand--back .brand__name { font-size: 34px; }
  .tagline {
    position: absolute;
    left: 40px; top: 215px;
    font-family: "Open Sans", Arial, sans-serif;
    font-weight: 700;
    font-size: 15px;
    line-height: 1.25;
    color: var(--green);
    text-align: center;
    width: 200px;
  }
  .map-frame {
    position: absolute;
    left: 282px; top: 52px;
    width: 228px; height: 192px;
    border: 3px solid var(--green);
    background: var(--gold);
    padding: 6px;
  }
  .map {
    width: 100%; height: 100%;
    background: linear-gradient(135deg, var(--map-base) 0%, var(--map-base) 70%, var(--map-park) 100%);
  }
</style>
</head>
<body>

<section class="card card--front" aria-label="Business card front">
  <svg class="wave" viewBox="0 0 540 310" preserveAspectRatio="none" aria-hidden="true">
    <path d="M0 232 C165 196 350 242 540 132 L540 310 L0 310 Z" fill="var(--gold)"/>
    <path d="M0 243 C165 210 350 255 540 147 L540 310 L0 310 Z" fill="#ffffff"/>
    <path d="M0 255 C165 225 350 265 540 162 L540 310 L0 310 Z" fill="var(--green)"/>
  </svg>

  <div class="brand">
    <span class="brand__square"></span>
    <span class="brand__name">The Stone Harbor</span>
  </div>

  <div class="divider"></div>

  <div class="person">
    <p class="person__name">Martin Cole</p>
    <p class="person__title">Owner</p>
  </div>

  <ul class="contact">
    <li>
      <svg viewBox="0 0 12 12" aria-hidden="true"><circle cx="6" cy="6" r="5.3" fill="none" stroke="#222" stroke-width="1"/><path d="M4 3.2 L5.2 3.2 L5.6 4.6 L4.9 5.2 Q5.6 6.6 6.8 7.1 L7.4 6.4 L8.8 6.8 L8.8 8 Q6.5 8.4 4.6 6.5 Q3.4 5 4 3.2 Z" fill="#222"/></svg>
      214-555-0183
    </li>
    <li>
      <svg viewBox="0 0 12 12" aria-hidden="true"><rect x="0.5" y="2.5" width="11" height="7.5" fill="#222"/><path d="M0.5 2.5 L6 7 L11.5 2.5" fill="none" stroke="#fff" stroke-width="1"/></svg>
      Martin.Cole@SHBexample.com
    </li>
  </ul>

  <p class="address">4832 Fenwick Oaks Blvd.<br>Dallas, Texas 75391</p>
</section>

<section class="card card--back" aria-label="Business card back">
  <div class="brand brand--back">
    <span class="brand__square"></span>
    <span class="brand__name">The Stone Harbor</span>
  </div>

  <p class="tagline">We Install And Supply<br>Granite Counter Tops</p>

  <div class="map-frame">
    <div class="map" role="img" aria-label="Maplio street map showing the store location on Fenwick Oaks Blvd., Dallas"></div>
  </div>
</section>

</body>
</html>
```